Need 2 sided card for Loomfield Goods Co. Logo supplied.

I am looking for a business card for my online craft supply business.

I have a very simple design already which I am kind of happy with (see attached pdf) - but would like suggestions for something a little more creative. Design MUST be clean. Super clean! Think thin lines and not blocks of color...

Design must be clean and crisp. No other colors other than in palette (see link below)

I would also like to possible incorporate my tagline - maybe on the front but definitely on the back:
"HobbyNest Ideas & Making Materials"

Logo file is supplied, but I think spacing on the card may required the wording to be moved underneaths the camera icon - which is fine. Font in logo is Maven Pro. OPEN TO USE OF OTHER FONTS ON CARD BUT MUST BE CLEAN DESIGN.

FRONT OF CARD
All information on attached pdf is correct and should be shown in your design.

BACK OF CARD
Needs to show www.tinselbrookstore.com and maybe logo repeat and tagline.

SIZE
New Zealand sized - meaning finished card will be 90 x 55mm
Printing requirements: printed area is 90mm x 55mm with a 2mm bleed all round.

COLORS
Color palette used in logo can be seen here for HEX and RGB reference: http://www.huegatherly.net/palette/8802417/website

NOTE: PAYMENT WILL BE MADE FOR THE BEST DESIGN - EVEN IF I DECIDE NOT TO USE IT.
Updates

Thank you all so much for your designs. I will be providing feedback to ALL designers tomorrow. This weekend is a holiday weekend here in New Zealand and so no work for a few days. Thank-you again - I appreciate your time and creativity!

Industry/Entity Type

Camera

Font styles to use
Other font styles liked:
• Maven Pro - open to others

Requirements
Must have
• Clean design. Logo must be prominent for brand recognition. All contact information must be shown.
Nice to have
• Tagline - at least on reverse

```html
<!DOCTYPE html>
<html lang="en">
<head>
<meta charset="utf-8">
<title>Loomfield Goods Co. – Business Card</title>
<link rel="stylesheet" href="https://fonts.googleapis.com/css2?family=Ubuntu:wght@400;500;700&display=swap">
<style>
  :root {
    --backdrop: #3a2b20;
    --card-white: #ffffff;
    --brand-yellow: #d8c626;
    --tagline-yellow: #cdbf1f;
    --ink-grey: #5e5a58;
    --icon-grey: #8b8680;
    --text-white: #ffffff;
    --watermark: rgba(225, 214, 120, 0.28);
    --watermark-light: rgba(255, 255, 255, 0.22);
  }
  * { margin: 0; padding: 0; box-sizing: border-box; }
  html, body {
    width: 1200px; height: 1000px; overflow: hidden;
    background: var(--backdrop);
    font-family: "Ubuntu", sans-serif;
  }
  .canvas { position: relative; width: 1200px; height: 1000px; }

  .card {
    position: absolute; top: 168px; width: 404px; height: 698px;
    border-radius: 30px; overflow: hidden;
  }
  .card--front { left: 180px; background: var(--card-white); }
  .card--back  { left: 584px; background: var(--brand-yellow); }

  .card__mark {
    position: absolute; width: 330px; height: 330px; border-radius: 50%;
    top: 370px;
  }
  .card--front .card__mark { left: 270px; background: var(--watermark); }
  .card--back  .card__mark { left: -134px; background: var(--watermark-light); }

  .brand {
    position: absolute; left: 40px; top: 100px;
    display: flex; align-items: center; gap: 12px;
  }
  .brand__square {
    width: 54px; height: 54px; border-radius: 8px; background: var(--ink-grey);
  }
  .brand__name {
    font-size: 30px; font-weight: 400; color: var(--ink-grey); letter-spacing: -0.2px;
  }
  .tagline {
    position: absolute; top: 163px; font-size: 17px; white-space: nowrap;
  }
  .card--front .tagline { left: 40px; color: var(--tagline-yellow); }
  .card--back .tagline { right: 32px; color: var(--ink-grey); }

  .holder-name {
    position: absolute; right: 32px; top: 106px;
    font-size: 37px; font-weight: 700; color: var(--text-white);
  }

  .contacts { position: absolute; list-style: none; bottom: 13px; }
  .contacts li {
    display: flex; align-items: center; gap: 10px;
    height: 31.5px; font-size: 18px; white-space: nowrap;
  }
  .card--front .contacts { left: 26px; color: var(--ink-grey); }
  .card--back .contacts { right: 22px; color: var(--text-white); }
  .card--back .contacts li { justify-content: flex-end; }
  .contact__icon { width: 24px; height: 24px; flex: none; }
</style>
</head>
<body>
<main class="canvas">

  <section class="card card--front" aria-label="Card front">
    <div class="card__mark" aria-hidden="true"></div>
    <div class="brand">
      <span class="brand__square" aria-hidden="true"></span>
      <span class="brand__name">Loomfield Goods Co.</span>
    </div>
    <p class="tagline">HobbyNest Ideas &amp; Making Materials</p>
    <ul class="contacts">
      <li>
        <svg class="contact__icon" viewBox="0 0 24 24" aria-hidden="true"><circle cx="12" cy="12" r="12" fill="#d8c626"/><circle cx="12" cy="12" r="4" fill="none" stroke="#fff" stroke-width="1.4"/></svg>
        pinwheel.nz/loomfield
      </li>
      <li>
        <svg class="contact__icon" viewBox="0 0 24 24" aria-hidden="true"><circle cx="12" cy="12" r="12" fill="#d8c626"/><rect x="7.5" y="9" width="9" height="8" rx="1" fill="#fff"/><path d="M9.8 9V7.6a2.2 2.2 0 0 1 4.4 0V9" fill="none" stroke="#fff" stroke-width="1.3"/></svg>
        www.tinselbrookstore.com
      </li>
      <li>
        <svg class="contact__icon" viewBox="0 0 24 24" aria-hidden="true"><circle cx="12" cy="12" r="12" fill="#d8c626"/><g fill="none" stroke="#fff" stroke-width="1.2"><circle cx="12" cy="12" r="6.5"/><ellipse cx="12" cy="12" rx="3" ry="6.5"/><line x1="5.5" y1="12" x2="18.5" y2="12"/><line x1="6.5" y1="8.8" x2="17.5" y2="8.8"/><line x1="6.5" y1="15.2" x2="17.5" y2="15.2"/></g></svg>
        www.loomfieldnz.com
      </li>
    </ul>
  </section>

  <section class="card card--back" aria-label="Card back">
    <div class="card__mark" aria-hidden="true"></div>
    <h1 class="holder-name">Wren Calloway</h1>
    <p class="tagline">HobbyNest Ideas &amp; Making Materials</p>
    <ul class="contacts">
      <li>
        +64 (0) 3 481 2267
        <svg class="contact__icon" viewBox="0 0 24 24" aria-hidden="true"><circle cx="12" cy="12" r="12" fill="#8b8680"/><path d="M8.3 6.5l2 2.6-1.2 1.4a8 8 0 0 0 4.4 4.4l1.4-1.2 2.6 2-1.3 1.8c-4.6.2-9.5-4.7-9.3-9.3z" fill="#fff" opacity="0.85"/></svg>
      </li>
      <li>
        +64 (0) 21 047 39186
        <svg class="contact__icon" viewBox="0 0 24 24" aria-hidden="true"><circle cx="12" cy="12" r="12" fill="#8b8680"/><rect x="8.5" y="5.5" width="7" height="13" rx="1.2" fill="none" stroke="#fff" stroke-width="1.3" opacity="0.85"/><circle cx="12" cy="16.3" r="0.9" fill="#fff"/></svg>
      </li>
      <li>
        wren.calloway@loomfieldnz.com
        <svg class="contact__icon" viewBox="0 0 24 24" aria-hidden="true"><circle cx="12" cy="12" r="12" fill="#8b8680"/><rect x="6.5" y="8" width="11" height="8" rx="1" fill="#fff" opacity="0.85"/><path d="M6.8 8.4L12 12.6l5.2-4.2" fill="none" stroke="#8b8680" stroke-width="1.1"/></svg>
      </li>
    </ul>
  </section>

</main>
</body>
</html>
```